Business card and stationary for consulting business

We need business cards and matching stationary for professional consulting business for employment and human resources issues.
One of the CraftHive designers designed the logo with our company name.  Use the colors in the logo and may use light yellow as an accent color.
Add
Mara T. Vollen, J.D., LL.M.
485 E. Callister Lane
Winter Park, Florida  32789
407-555-0183
maravollenjd@quillpost.example

Industry/Entity Type
Business

```html
<!DOCTYPE html>
<html lang="en">
<head>
<meta charset="utf-8">
<title>Northvale HR — Business Card</title>
<link rel="stylesheet" href="https://fonts.googleapis.com/css2?family=Quicksand:wght@400;500&family=Lato:wght@400;700&display=swap">
<style>
  :root {
    --cyan: #04f9f9;
    --brand-blue: #1f6fa6;
    --frame-grey: #cdcdcd;
    --paper: #ffffff;
    --ink: #1a1a1a;
    --backdrop: #ece8e3;
  }
  html, body {
    margin: 0;
    padding: 0;
    width: 1200px;
    height: 1000px;
    overflow: hidden;
    background: var(--backdrop);
  }
  .canvas {
    position: relative;
    width: 1200px;
    height: 1000px;
  }
  .card {
    position: absolute;
    left: 239px;
    width: 722px;
    height: 423px;
    box-shadow: 0 6px 18px rgba(0,0,0,0.18);
    overflow: hidden;
  }
  .card--front { top: 66px; background: var(--cyan); }
  .card--back { top: 510px; background: var(--frame-grey); }

  .card-frame { position: absolute; inset: 0; }

  .lockup {
    position: absolute;
    left: 147px;
    display: flex;
    align-items: center;
  }
  .lockup__name {
    font-family: "Quicksand", sans-serif;
    font-weight: 500;
    font-size: 41px;
    letter-spacing: -0.3px;
    line-height: 1;
    padding-right: 18px;
    white-space: nowrap;
  }
  .lockup__rule {
    width: 2px;
    height: 96px;
    margin-right: 10px;
  }
  .lockup__tagline {
    font-family: "Quicksand", sans-serif;
    font-weight: 400;
    font-size: 17px;
    line-height: 21px;
    white-space: nowrap;
  }
  .card--front .lockup { top: 164px; }
  .card--front .lockup__name,
  .card--front .lockup__tagline { color: var(--paper); }
  .card--front .lockup__rule { background: var(--paper); }

  .card--back .lockup { top: 163px; }
  .card--back .lockup__name,
  .card--back .lockup__tagline { color: var(--brand-blue); }
  .card--back .lockup__rule { background: var(--frame-grey); }

  .holder {
    position: absolute;
    top: 46px;
    right: 47px;
    text-align: right;
    font-family: "Lato", sans-serif;
  }
  .holder__name {
    color: var(--brand-blue);
    font-weight: 700;
    font-size: 20px;
    line-height: 24px;
  }
  .holder__credentials {
    color: var(--ink);
    font-size: 15px;
    line-height: 20px;
  }
  .contact {
    position: absolute;
    top: 321px;
    font-family: "Lato", sans-serif;
    font-style: normal;
    font-size: 17px;
    line-height: 24px;
    color: var(--ink);
    white-space: nowrap;
  }
  .contact--address { left: 59px; }
  .contact--reach { right: 53px; }
</style>
</head>
<body>
<main class="canvas">

  <section class="card card--front" aria-label="Card front">
    <div class="lockup">
      <span class="lockup__name">Northvale HR</span>
      <span class="lockup__rule"></span>
      <div class="lockup__tagline">
        <div>Support People</div>
        <div>Simplify Policy</div>
        <div>Reduce Risk</div>
      </div>
    </div>
  </section>

  <section class="card card--back" aria-label="Card back">
    <svg class="card-frame" width="722" height="423" viewBox="0 0 722 423" aria-hidden="true">
      <rect width="722" height="423" fill="var(--frame-grey)"/>
      <polygon points="0,0 166,0 0,166" fill="var(--cyan)"/>
      <polygon points="166,0 191,0 0,191 0,166" fill="var(--paper)"/>
      <polygon points="722,423 556,423 722,257" fill="var(--cyan)"/>
      <polygon points="556,423 531,423 722,232 722,257" fill="var(--paper)"/>
      <rect x="31" y="31" width="660" height="361" fill="var(--paper)"/>
    </svg>

    <div class="holder">
      <div class="holder__name">Mara T. Vollen</div>
      <div class="holder__credentials">J.D., LL.M.</div>
    </div>

    <div class="lockup">
      <span class="lockup__name">Northvale HR</span>
      <span class="lockup__rule"></span>
      <div class="lockup__tagline">
        <div>Support People</div>
        <div>Simplify Policy</div>
        <div>Reduce Risk</div>
      </div>
    </div>

    <address class="contact contact--address">
      <div>485 E. Callister Lane</div>
      <div>Cedar Hollow, Florida 32871</div>
    </address>
    <div class="contact contact--reach">
      <div>407-555-0183</div>
      <div>maravollenjd@quillpost.example</div>
    </div>
  </section>

</main>
</body>
</html>
```